Real Estate Open House A Frame Sign

The sign is 22" wide and 28" tall. This sign is used to post around the neighbourhood to direct people to an open house (home that is for sale). It is also used for self-promotion.

Designwise
- I just want something with a modern look, simple and clean.
- I want my picture and business logo on the left side.
- On the right side, website (www.lumwick-realestate.com) and my phone (555-374-9126), then a blank space where I can write an address when I need to.

I'm not sure how I want the overall design look. I'm very open-minded and I'm depending on your creative mind to come up with something.

If you have any questions, please let me know.

```html
<!DOCTYPE html>
<html lang="en">
<head>
<meta charset="utf-8">
<title>Lumwick Real Estate – Open House Sign</title>
<link rel="stylesheet" href="https://fonts.googleapis.com/css2?family=Montserrat:wght@300;400&family=Roboto+Condensed:wght@700&display=swap">
<style>
  :root {
    --navy: #1c4580;
    --navy-light: #2f5a96;
    --white: #ffffff;
    --photo-dark: #3a3f47;
    --photo-light: #c9ccd1;
  }
  html, body {
    margin: 0;
    padding: 0;
    overflow: hidden;
    background: var(--white);
  }
  .sign {
    position: relative;
    width: 943px;
    height: 1200px;
    overflow: hidden;
    background: var(--white);
  }
  .sign__art {
    position: absolute;
    inset: 0;
    width: 943px;
    height: 1200px;
  }
  .brand {
    position: absolute;
    left: 34px;
    top: 58px;
    color: var(--white);
    font-family: "Montserrat", sans-serif;
    font-weight: 300;
  }
  .brand__name {
    display: block;
    font-size: 78px;
    line-height: 1;
    letter-spacing: 0.04em;
  }
  .brand__tag {
    display: block;
    margin-top: 20px;
    font-size: 24px;
    letter-spacing: 0.32em;
  }
  .contact {
    position: absolute;
    left: 250px;
    width: 690px;
    text-align: center;
    color: var(--navy);
    font-family: "Roboto Condensed", sans-serif;
    font-weight: 700;
    line-height: 1;
  }
  .contact--web {
    top: 366px;
    font-size: 52px;
  }
  .contact--phone {
    top: 462px;
    font-size: 96px;
    letter-spacing: 0.01em;
  }
</style>
</head>
<body>
<main class="sign">
  <svg class="sign__art" viewBox="0 0 786 1000" preserveAspectRatio="none" aria-hidden="false">
    <defs>
      <linearGradient id="portraitTone" x1="0" y1="0" x2="0" y2="1">
        <stop offset="0" stop-color="var(--photo-light)"/>
        <stop offset="0.35" stop-color="#8a8f97"/>
        <stop offset="1" stop-color="var(--photo-dark)"/>
      </linearGradient>
    </defs>

    <!-- header swooshes -->
    <path class="header-band" d="M0,0 L555,0 C470,110 280,200 0,222 Z" fill="var(--navy)"/>
    <path class="header-line" d="M0,238 C260,226 560,120 730,0" fill="none" stroke="var(--navy)" stroke-width="4"/>
    <path class="header-swoosh" d="M786,18 L786,92 C640,170 470,232 285,266 C470,214 640,128 786,18 Z" fill="var(--navy-light)"/>
    <path class="header-line" d="M0,256 C300,254 600,205 786,118" fill="none" stroke="var(--navy)" stroke-width="2.5"/>

    <!-- divider and address lines -->
    <rect class="divider" x="0" y="497" width="786" height="7" fill="var(--navy)"/>
    <g class="address-lines" stroke="var(--navy)" stroke-width="2.5">
      <line x1="195" y1="577" x2="750" y2="577"/>
      <line x1="230" y1="629" x2="750" y2="629"/>
      <line x1="265" y1="686" x2="750" y2="686"/>
      <line x1="300" y1="740" x2="750" y2="740"/>
      <line x1="330" y1="797" x2="750" y2="797"/>
    </g>

    <!-- agent portrait area -->
    <path class="portrait" role="img" aria-label="Portrait photo of the agent in a dark suit, arms crossed"
          d="M40,320 H215 V560 L300,640 L360,860 L360,1000 H0 V560 Z" fill="url(#portraitTone)"/>

    <!-- footer swooshes -->
    <path class="footer-swoosh" d="M0,1000 C120,920 330,872 500,850 C330,888 150,948 60,1000 Z" fill="var(--navy-light)"/>
    <path class="footer-line" d="M180,1000 C350,905 600,855 786,850" fill="none" stroke="var(--navy)" stroke-width="3"/>
    <path class="footer-band" d="M260,1000 C450,922 620,892 786,885 V1000 Z" fill="var(--navy)"/>
  </svg>

  <div class="brand">
    <span class="brand__name">LUMWICK</span>
    <span class="brand__tag">REAL ESTATE</span>
  </div>

  <div class="contact contact--web">www.lumwick-realestate.com</div>
  <div class="contact contact--phone">555-374-9126</div>
</main>
</body>
</html>
```